Check-up reminder postcard

We require a design for a postcard to remind patients to book their dental check up.

Size: standard postcard 100 x 150mm

We are a small family-focussed dental practice. The design should reflect our brand which is warm & sophisticated as well as incorporate the logo colours. For more information please see our website kellowayfamilydental.com.au.

Target Market(s)

Female aged 30 - 45 years old

Industry/Entity Type

Dental

Requirements
Must have
• The front side should have the copy "We've been missing you...".

Back side of postcard should have area for patient name, address, stamp to be placed. The following copy should be used:

"Dear (please leave space for name)

We've been missing you!

We haven't seen you for your regular dental check up. Please call or visit our website to schedule an appointment. Alternatively, we will be in touch over the next couple of weeks.

We look forward to seeing you again soon!

The Kelloway Family Dental team

Phone: 03 9412 7058 Address: 118 Denholm Road, Kelloway VIC 3152 Web: www.kellowayfamilydental.com.au Email: admin@kellowayfamilydental.com.au"

Include the logo on back side of postcard. Please add the tag line under the logo "Creating beautiful smiles everyday" - sans serif font.

- Design file:
All colours must be converted to CMYK.
Bleed 3mm external from trim.
Trims and registration marks are offset 5mm.
All text to be 3mm from trim if possible.
Nice to have
• Maple leaf as in the logo
Slightly cursive font
Less cluttered look
Should not have
• Cartoons
Pictures of teeth, drills, probes, mirrors
Photos of people

```html
<!DOCTYPE html>
<html lang="en">
<head>
<meta charset="utf-8">
<title>Kelloway Family Dental — Check-up Reminder Postcard</title>
<link rel="stylesheet" href="https://fonts.googleapis.com/css2?family=EB+Garamond:wght@500&family=Open+Sans:ital,wght@1,300&display=swap">
<style>
  :root {
    --paper: #ffffff;
    --teal: #138a8e;
    --olive-soft: #cfd08a;
    --leaf-green: #8fa83a;
    --slate: #6f6f66;
  }
  html, body {
    margin: 0;
    padding: 0;
    width: 1200px;
    height: 799px;
    overflow: hidden;
    background: var(--paper);
  }
  .postcard {
    position: relative;
    width: 1200px;
    height: 799px;
    background: var(--paper);
  }
  .brand {
    position: absolute;
    left: 54px;
    top: 44px;
    display: flex;
    align-items: center;
    gap: 16px;
  }
  .brand-dot {
    width: 66px;
    height: 66px;
    border-radius: 50%;
    background: var(--leaf-green);
    margin-top: 60px;
  }
  .brand-name {
    font-family: "EB Garamond", serif;
    font-weight: 500;
    font-size: 44px;
    line-height: 1.05;
    color: var(--teal);
    margin: 0;
  }
  .quote-mark {
    position: absolute;
    fill: var(--olive-soft);
  }
  .quote-open { left: 117px; top: 277px; }
  .quote-close { left: 917px; top: 287px; }
  .headline {
    position: absolute;
    left: 260px;
    top: 384px;
    margin: 0;
    font-family: "EB Garamond", serif;
    font-weight: 500;
    font-size: 64px;
    line-height: 1;
    color: var(--teal);
    white-space: nowrap;
  }
  .tagline {
    position: absolute;
    right: 67px;
    top: 712px;
    margin: 0;
    font-family: "Open Sans", sans-serif;
    font-style: italic;
    font-weight: 300;
    font-size: 28px;
    line-height: 1;
    color: var(--slate);
    white-space: nowrap;
  }
</style>
</head>
<body>
  <main class="postcard">
    <header class="brand">
      <span class="brand-dot" aria-hidden="true"></span>
      <p class="brand-name">Kelloway<br>Family Dental</p>
    </header>

    <svg class="quote-mark quote-open" width="164" height="114" viewBox="0 0 164 114" aria-hidden="true">
      <path d="M66 4 C32 16 4 44 4 76 C4 98 18 112 38 112 C56 112 68 99 68 83 C68 65 54 55 36 57 C38 37 50 20 72 10 Z"/>
      <path transform="translate(88 0)" d="M66 4 C32 16 4 44 4 76 C4 98 18 112 38 112 C56 112 68 99 68 83 C68 65 54 55 36 57 C38 37 50 20 72 10 Z"/>
    </svg>

    <h1 class="headline">We've been missing you.</h1>

    <svg class="quote-mark quote-close" width="164" height="114" viewBox="0 0 164 114" aria-hidden="true">
      <g transform="rotate(180 82 57)">
        <path d="M66 4 C32 16 4 44 4 76 C4 98 18 112 38 112 C56 112 68 99 68 83 C68 65 54 55 36 57 C38 37 50 20 72 10 Z"/>
        <path transform="translate(88 0)" d="M66 4 C32 16 4 44 4 76 C4 98 18 112 38 112 C56 112 68 99 68 83 C68 65 54 55 36 57 C38 37 50 20 72 10 Z"/>
      </g>
    </svg>

    <p class="tagline">Creating beautiful smiles everyday</p>
  </main>
</body>
</html>
```